The Lumo-Hub for Rescue Drills + Crowd Care Post Card

Hi! I am a new business that is Licensed Training Provider to the National Bluefield Aid. We teach private CPR/AED, First Aid and a variety of other emergency training courses to the general public! Our goal is to get into businesses of all sizes from the mom and pops store to corporate offices of Manhattan. We can do private classes in your home and no office space is to small! We even have a school assembly program that teaches "Hands Only CPR" for children. I'm looking to make a post card to hand out that can easily explain what we are doing…that might have some good visuals that catch your eye as well. I def want to use The Lumo Hub logo in it that I have attached. Im not necessarily married to any of the other images. You can check out our website www.lumohubdrills.example for more information and you can use any of the images on there as well if you would like. I will give you free reign to find any cool photo stock image that you might think fits with what I'm trying to do. Hopefully you can help!
Updates

Also feel free to use any other photos that you might find that you think fit our cause for teaching CPR/First aid etc!! Thanks!

Thank you all for your hard work. I actually like many of these designs and really torn! I will be making some decisions in the next day or so. Thank you! Wendel

Industry/Entity Type

Training

```html
<!DOCTYPE html>
<html lang="en">
<head>
<meta charset="utf-8">
<title>The Lumo Hub Post Card</title>
<link rel="stylesheet" href="https://fonts.googleapis.com/css2?family=Open+Sans:wght@400;600;700;800&family=Roboto+Condensed:wght@400;700&display=swap">
<style>
:root{
  --bg:#ececec;
  --red:#e8202a;
  --dark:#231f20;
  --white:#ffffff;
  --ink:#231f20;
  --photo-a:#3a3436;
  --photo-b:#7a6f73;
  --photo-c:#c9b8ae;
  --portrait:#6b6463;
}
*{margin:0;padding:0;box-sizing:border-box}
html,body{width:1200px;height:1000px;overflow:hidden;background:var(--bg);font-family:"Open Sans",sans-serif}
.card{position:absolute;overflow:hidden;background:var(--white)}
.front{left:377px;top:116px;width:471px;height:364px}
.back{left:371px;top:511px;width:476px;height:368px;background:var(--red)}
.abs{position:absolute}
.shapes{position:absolute;left:0;top:0}
.brand{display:flex;align-items:center;gap:6px;color:var(--white);font-weight:600;font-size:22px;letter-spacing:-.3px;white-space:nowrap}
.brand-mark{width:10px;height:10px;background:var(--red)}
.contact-top{left:275px;top:12px;color:var(--white);display:flex;gap:7px}
.contact-top .lbl{font-size:8px;font-weight:800}
.contact-top .phone{font-size:16px;font-weight:800;line-height:17px}
.contact-top .web{font-size:11px;line-height:11px}
.hero-photo{left:0;top:57px;width:471px;height:222px;background:linear-gradient(100deg,var(--photo-a) 0%,var(--photo-b) 45%,var(--photo-c) 70%,var(--photo-a) 100%)}
.headline-small{left:16px;top:130px;color:var(--white);font-weight:800;font-size:17px}
.headline-big{left:12px;top:145px;color:var(--red);font-weight:800;font-size:78px;line-height:78px;letter-spacing:-2px}
.pitch{right:14px;top:186px;text-align:right;font-size:10px;font-weight:700;line-height:12.5px;color:var(--ink);text-transform:uppercase}
.pitch .hl{color:var(--red)}
.promo{left:16px;top:233px;color:var(--white);font-size:10px;line-height:12px;font-weight:600;text-transform:uppercase;width:190px}
.promo b{font-weight:800}
.schools{right:19px;top:232px;color:var(--white);text-align:right;font-size:9.5px;line-height:11.5px;font-weight:600;text-transform:uppercase}
.schools b{font-weight:800}
.badge{background:var(--red);opacity:.9}
.about{left:17px;top:22px;width:265px;font-size:9.5px;line-height:11.8px;color:var(--ink)}
.about .hl{color:var(--red);font-weight:800}
.services-title{left:17px;top:120px;color:var(--red);font-weight:800;font-size:9.5px}
.services{left:17px;top:135px;list-style:none;font-size:9.5px;line-height:11.9px;color:var(--ink)}
.services li{padding-left:16px;position:relative}
.services li::before{content:"+";position:absolute;left:2px;top:-2px;color:var(--red);font-weight:800;font-size:13px}
.portrait{left:353px;top:22px;width:95px;height:143px;background:linear-gradient(180deg,#8b8482,var(--portrait) 60%,#4a4546)}
.bio{right:27px;top:172px;text-align:right;color:var(--white);font-family:"Roboto Condensed",sans-serif;font-size:9px;line-height:12px;white-space:nowrap}
.bio b{font-size:11px;font-weight:700}
.booking{right:27px;top:262px;text-align:right;color:var(--white);font-weight:800;font-size:9px;line-height:11px;text-transform:uppercase}
.owner{right:27px;top:298px;text-align:right;color:var(--white);font-size:10.5px;line-height:12.5px}
.owner b{font-size:11.5px;font-weight:800}
</style>
</head>
<body>
<section class="card front">
  <svg class="shapes" width="471" height="364" aria-hidden="true">
    <rect x="0" y="0" width="471" height="57" fill="#231f20"/>
    <polygon points="262,0 471,0 471,57 232,57" fill="#e8202a"/>
  </svg>
  <div class="abs brand" style="left:24px;top:15px"><span class="brand-mark"></span>The Lumo Hub</div>
  <div class="abs contact-top">
    <svg width="14" height="28" viewBox="0 0 14 28" aria-hidden="true"><path d="M3 2 L7 2 L8 8 L5 10 Q5 17 8 20 L11 18 L13 24 L10 27 Q2 24 1 14 Q1 5 3 2Z" fill="#fff"/></svg>
    <div><div class="lbl">CONTACT US TODAY:</div><div class="phone">+1 555-014-2260</div><div class="web">www.lumohubdrills.example</div></div>
  </div>
  <div class="abs hero-photo" role="img" aria-label="Photo of gloved hands practising CPR on a training manikin with a breathing mask"></div>
  <svg class="shapes" width="471" height="364" aria-hidden="true">
    <defs><linearGradient id="lite" x1="0" x2="1"><stop offset="0" stop-color="#fff" stop-opacity="0"/><stop offset=".3" stop-color="#fff" stop-opacity=".75"/><stop offset="1" stop-color="#fff" stop-opacity=".8"/></linearGradient></defs>
    <rect x="210" y="180" width="261" height="48" fill="url(#lite)"/>
    <rect x="170" y="228" width="301" height="51" fill="#231f20"/>
    <polygon points="0,228 210,228 190,279 0,279" fill="#e8202a"/>
  </svg>
  <div class="abs headline-small">LEARN TO SAVE A</div>
  <div class="abs headline-big">LIFE</div>
  <div class="abs pitch"><span class="hl">The Lumo Hub</span> is a leading provider of<br>safety and emergency preparedness<br>training + event safety managent</div>
  <div class="abs promo">Learn how <b>to save a life</b> today in our variety of emergency preparation courses!</div>
  <div class="abs schools"><b>Specialized programs for schools:</b><br>- First aid for student<br>- CPR for students<br>- First aid and CPR for student</div>
  <div class="abs badge" style="left:10px;top:290px;width:110px;height:60px" role="img" aria-label="Partner campaign badge"></div>
  <div class="abs badge" style="left:128px;top:290px;width:112px;height:60px" role="img" aria-label="Partner preparedness badge"></div>
</section>

<section class="card back">
  <svg class="shapes" width="476" height="368" aria-hidden="true">
    <polygon points="0,0 305,0 250,300 0,300" fill="#ffffff"/>
    <polygon points="0,300 262,300 250,368 0,368" fill="#231f20"/>
  </svg>
  <p class="abs about"><span class="hl">THE LUMO HUB</span> for Rescue Drills &amp; Consulting is a Limited Liability Corporation organized under the laws of the State of New York. Our highly qualified instructors &amp; independent contractors hold numerous certifications &amp; licenses from various Government Agencies and Organizations. We take pride in our services, &amp; hold ourselves to the highest level of professionalism for all events.</p>
  <div class="abs services-title">SERVICE WE PROVIDE:</div>
  <ul class="abs services">
    <li>National Certification in variety of CPR<br>/AED / FIRST AID / O2 Courses</li>
    <li>National Bluefield Aid Lifeguard Training</li>
    <li>Lifeguards for all events</li>
    <li>Rescue board rentals</li>
    <li>Marine safety coordination</li>
    <li>Certified rescue drivers</li>
    <li>Communication rentals</li>
    <li>Customized emergency action plans</li>
    <li>First AID kits / Supplies</li>
    <li>Athletic trainers</li>
    <li>Safety walk throughs</li>
    <li>Fireguards</li>
  </ul>
  <div class="abs brand" style="left:26px;top:320px"><span class="brand-mark"></span>The Lumo Hub</div>
  <div class="abs portrait" role="img" aria-label="Portrait photo of the owner and founder"></div>
  <p class="abs bio">owner and founder of the <b>THE LUMO HUB,</b><br><b>WENDEL MARLOW</b> is an expert in his field.<br>17 Years as a emergency medical technician<br>and ocean lifeguard with the perstigious<br>HARBOR POINT LIFEGUARD CORPS, Wendel brings<br>a wealth of knowledge and experience<br>to all of his clients.</p>
  <div class="abs booking">For more information on<br>booking the Lumo Hub for<br>your event, contact:</div>
  <div class="abs owner"><b>WENDEL MARLOW</b><br>P: +1 555-014-2260<br>E: desk@lumohubdrills.example<br>www.lumohubdrills.example</div>
</section>
</body>
</html>
```